Business Card Design

i am looking a business card for a car rental company long with Taxi service also a logo.
Updates

what is the latest with my project

Industry/Entity Type

Business

Contact Information for Business Card

name of the Company is Brenmoor Auto Hire and Cab Services
Address: Harlow Cove Village, St. Wren's Parish Antigua
Tele# 558-2047/6194852-613-9075
Email: tolvipark@quenmail.net

Font styles to use
Script

```html
<!DOCTYPE html>
<html lang="en">
<head>
<meta charset="utf-8">
<title>Brenmoor Auto Hire and Cab Services – Business Card</title>
<link rel="stylesheet" href="https://fonts.googleapis.com/css2?family=Open+Sans:wght@400;600&display=swap">
<style>
  :root {
    --backdrop: #1c1c1c;
    --card: #ffffff;
    --ink: #1a1a1a;
    --brand-green: #109a4f;
    --rule-blue: #c9d6ec;
    --rule-green: #7cc79a;
  }
  * { margin: 0; padding: 0; box-sizing: border-box; }
  html, body {
    width: 1200px; height: 900px; overflow: hidden;
    background: var(--backdrop);
    font-family: "Open Sans", Arial, sans-serif;
  }
  .canvas {
    position: relative; width: 1200px; height: 900px;
    display: flex; align-items: center; justify-content: center;
  }
  .card {
    position: relative; width: 980px; height: 560px;
    background: var(--card);
    color: var(--ink);
  }
  .company-title {
    position: absolute; top: 78px; left: 250px; right: 80px;
    font-size: 30px; font-weight: 400; text-align: center;
    letter-spacing: 0.2px;
  }
  .title-rule {
    position: absolute; top: 150px; left: 450px; right: 90px;
    height: 1px; background: var(--rule-blue);
  }
  .holder-name {
    position: absolute; top: 118px; right: 100px;
    font-size: 22px; font-weight: 400; color: var(--brand-green);
    letter-spacing: 1px;
  }
  .brand-mark {
    position: absolute; top: 255px; left: 70px; width: 360px;
    display: flex; align-items: center; gap: 14px;
  }
  .brand-mark .dot {
    width: 26px; height: 26px; border-radius: 50%;
    background: var(--brand-green); flex: none;
  }
  .brand-mark .brand-name {
    font-size: 56px; font-weight: 600; color: var(--brand-green);
    line-height: 1;
  }
  .brand-rule {
    position: absolute; top: 352px; left: 70px; width: 360px;
    height: 1px; background: var(--rule-green);
  }
  .contact-list {
    position: absolute; top: 270px; right: 70px;
    list-style: none; text-align: right;
    font-size: 19px; line-height: 1;
  }
  .contact-list li {
    display: flex; justify-content: flex-end; align-items: center;
    gap: 14px; margin-bottom: 18px;
  }
  .contact-list svg { width: 18px; height: 18px; fill: var(--brand-green); flex: none; }
</style>
</head>
<body>
<main class="canvas">
  <section class="card">
    <h1 class="company-title">Brenmoor Auto Hire and Cab Services</h1>
    <p class="holder-name">TOLVIPARK</p>
    <div class="title-rule"></div>

    <div class="brand-mark">
      <span class="dot"></span>
      <span class="brand-name">Brenmoor</span>
    </div>
    <div class="brand-rule"></div>

    <ul class="contact-list">
      <li>558-2047/6194852-613-9075
        <svg viewBox="0 0 24 24" aria-hidden="true"><path d="M6.6 10.8a15.1 15.1 0 0 0 6.6 6.6l2.2-2.2a1 1 0 0 1 1-.25 11.4 11.4 0 0 0 3.6.57 1 1 0 0 1 1 1V20a1 1 0 0 1-1 1A17 17 0 0 1 3 4a1 1 0 0 1 1-1h3.5a1 1 0 0 1 1 1c0 1.25.2 2.45.57 3.6a1 1 0 0 1-.25 1z"/></svg>
      </li>
      <li>tolvipark@quenmail.net
        <svg viewBox="0 0 24 24" aria-hidden="true"><path d="M2 5h20v14H2z M3.5 6.5 12 12.5l8.5-6" fill="none" stroke="#109a4f" stroke-width="2"/><path d="M2 5h20v14H2z"/><path d="M3 6l9 6.5L21 6" fill="none" stroke="#fff" stroke-width="1.6"/></svg>
      </li>
      <li>Harlow Cove Village, St. Wren's Parish Antigua
        <svg viewBox="0 0 24 24" aria-hidden="true"><path d="M12 2a7 7 0 0 0-7 7c0 5.2 7 13 7 13s7-7.8 7-13a7 7 0 0 0-7-7zm0 9.5A2.5 2.5 0 1 1 12 6.5a2.5 2.5 0 0 1 0 5z"/></svg>
      </li>
    </ul>
  </section>
</main>
</body>
</html>
```